Business Card Design Project

I need a business card for an environmentally friendly interior design company called Roomcraft Willow.
I was thinking it might be nice to print the business cards on brown recycled paper with green ink.
In addition to interior design, I will also be able to consult with homeowners regarding their indoor environments and how they might be affecting their health after May 2013 which is when I will complete my certification program. This can be added to the business card at that time: "Certified Habitat Vitalis Dwelling Consultant".
Health

```html
<!DOCTYPE html>
<html lang="en">
<head>
<meta charset="utf-8">
<title>Roomcraft Willow – Business Card</title>
<link rel="stylesheet" href="https://fonts.googleapis.com/css2?family=Exo+2:wght@300;400;500;700&display=swap">
<style>
  :root {
    --page-bg: #e7e8e6;
    --paper: #d8dfd3;
    --paper-light: #e0e6dc;
    --brand-green: #2b6a1e;
    --tagline-green: #3e8c2c;
    --name-green: #6cb04e;
    --title-grey: #434a4c;
    --contact-grey: #9fabad;
    --contact-label: #8d9a9c;
  }

  * { box-sizing: border-box; margin: 0; padding: 0; }

  html, body {
    width: 1200px;
    height: 900px;
    overflow: hidden;
  }

  body {
    background: var(--page-bg);
    font-family: "Exo 2", sans-serif;
    position: relative;
  }

  .business-card {
    position: absolute;
    left: 118px;
    top: 126px;
    width: 964px;
    height: 620px;
    background: radial-gradient(ellipse at 40% 35%, var(--paper-light), var(--paper) 75%);
  }

  .brand-name {
    position: absolute;
    left: 68px;
    top: 88px;
    font-size: 96px;
    font-weight: 700;
    line-height: 1;
    color: var(--brand-green);
    letter-spacing: -0.5px;
    white-space: nowrap;
  }

  .brand-tagline {
    position: absolute;
    left: 209px;
    top: 180px;
    font-size: 43px;
    font-weight: 500;
    line-height: 1;
    color: var(--tagline-green);
    white-space: nowrap;
  }

  .contact-block {
    position: absolute;
    left: 74px;
    top: 420px;
  }

  .person-name {
    font-size: 38px;
    font-weight: 400;
    line-height: 1;
    color: var(--name-green);
    white-space: nowrap;
  }

  .person-title {
    margin-top: 14px;
    font-size: 26px;
    font-weight: 400;
    line-height: 1;
    color: var(--title-grey);
    white-space: nowrap;
  }

  .contact-line {
    margin-top: 32px;
    font-size: 27px;
    font-weight: 300;
    line-height: 1;
    color: var(--contact-grey);
    white-space: nowrap;
  }

  .contact-label {
    font-weight: 700;
    color: var(--contact-label);
  }

  .contact-divider {
    font-weight: 700;
    color: var(--title-grey);
    margin: 0 18px;
  }
</style>
</head>
<body>
  <main class="business-card">
    <h1 class="brand-name">Roomcraft Willow</h1>
    <p class="brand-tagline">Environmentally friendly design</p>

    <section class="contact-block">
      <p class="person-name">Dana Lee Marsh</p>
      <p class="person-title">Certified Habitat Vitalis Dwelling Consultant</p>
      <p class="contact-line">
        <span class="contact-label">T:</span> 555-201-3847<span class="contact-divider">|</span><span class="contact-label">E:</span> xxxxxx@xxxxxx.com
      </p>
    </section>
  </main>
</body>
</html>
```